Business card design for a dynamic IT consulting company

We need a business card design for a young firm, specialized in the Telecommunications/Consulting industry. The name of the company is Brask and Partners Business Consulting Ltd. (Short name: Brask and Partnes)
Brask = solve read reverse, so we aim to be uncomplicated and solution-oriented. The small pipe in our logo is also related to the word solve. So we need a new business card design, which is simple, eye catching and something non traditional (I would probably prefer a square shaped design rather than a rectangle, but open for suggestions). Attached our logo.

Target Market(s)

Usually our customers are Tier1 Telecoms providers (Q-Linkra, Parnexo, etc) and their executives.

Industry/Entity Type

Business

Contact Information for Business Card

Name: Gergely Halmindo
Email: g.halmindo@braskpartnera.hu
Web: www.braskpartnera.hu
Mobile: +36 30 555 0192
Title: Managing Director

Optional:
Company name: Brask and Partners Ltd.
Address: 1047 Budapest, Ravaszi str. 17/B, Hungary

Font styles to use
Other font styles liked:
• helveticaneue_medium, Prime Regular are used now.

Colors

Designer to choose colors to be used in the design.

Requirements
Must have
• I would like to have a 2 sided design.
Nice to have
• I thought if we make the logo a bit bigger (without the company name), that could go to the back with the company name below. I though, if the pipe in the logo is somehow touchable on the business card, would be nice and unique.

```html
<!DOCTYPE html>
<html lang="en">
<head>
<meta charset="utf-8">
<title>Brask &amp; Partners – Business Card</title>
<link href="https://fonts.googleapis.com/css2?family=Lato:wght@400;700&family=Montserrat:wght@300;700&display=swap" rel="stylesheet">
<style>
  :root {
    --stage: #ececec;
    --card-dark: #2b2b2c;
    --card-white: #ffffff;
    --band-grey: #efefef;
    --ink: #3a3a3a;
    --ink-soft: #555555;
    --paper-text: #f4f4f4;
    --accent-blue: #2d9ad8;
    --icon-ring: #d8d8d8;
  }
  * { box-sizing: border-box; margin: 0; padding: 0; }
  html, body { width: 1200px; height: 768px; overflow: hidden; }
  body {
    background: var(--stage);
    display: flex;
    align-items: center;
    justify-content: center;
    gap: 20px;
    font-family: "Lato", Arial, sans-serif;
  }
  .card {
    width: 570px;
    height: 320px;
    flex: none;
    box-shadow: 0 6px 18px rgba(0,0,0,0.18);
    overflow: hidden;
    position: relative;
  }

  /* Front */
  .card-front { display: flex; background: var(--card-white); }
  .identity-panel {
    width: 200px;
    flex: none;
    background: var(--card-dark);
    color: var(--paper-text);
    padding: 78px 0 0 26px;
  }
  .person-first {
    font-family: "Montserrat", Arial, sans-serif;
    font-weight: 700;
    font-size: 22px;
    letter-spacing: 1px;
    line-height: 1.2;
  }
  .person-last {
    font-family: "Montserrat", Arial, sans-serif;
    font-weight: 300;
    font-size: 21px;
    letter-spacing: 1px;
    line-height: 1.2;
    margin-top: 2px;
  }
  .person-title {
    display: inline-block;
    margin-top: 10px;
    background: var(--accent-blue);
    color: #fff;
    font-size: 11.5px;
    padding: 4px 10px;
  }
  .info-panel { flex: 1; min-width: 0; display: flex; flex-direction: column; }
  .brand-band {
    height: 150px;
    flex: none;
    background: var(--band-grey);
    display: flex;
    align-items: center;
    padding-left: 34px;
    gap: 10px;
  }
  .brand-square { width: 12px; height: 12px; background: var(--accent-blue); flex: none; }
  .brand-name { font-size: 27px; color: var(--ink); font-weight: 400; white-space: nowrap; }
  .contact-grid {
    flex: 1;
    display: grid;
    grid-template-columns: minmax(0, 1fr) minmax(0, 1fr);
    column-gap: 10px;
    row-gap: 9px;
    padding: 22px 14px 0 18px;
    align-content: start;
  }
  .contact-item {
    display: flex;
    align-items: center;
    gap: 6px;
    font-size: 9.5px;
    line-height: 1.3;
    color: var(--ink-soft);
    min-width: 0;
  }
  .contact-text { min-width: 0; overflow-wrap: anywhere; }
  .contact-icon {
    width: 18px; height: 18px; flex: none;
    border-radius: 50%;
    border: 1px solid var(--icon-ring);
    display: flex; align-items: center; justify-content: center;
  }
  .contact-icon svg { width: 10px; height: 10px; fill: var(--ink); }

  /* Back */
  .card-back {
    background: var(--card-dark);
    display: flex;
    align-items: center;
    justify-content: center;
    gap: 12px;
  }
  .card-back .brand-square { width: 16px; height: 16px; }
  .card-back .brand-name { color: var(--paper-text); font-size: 36px; }
</style>
</head>
<body>

  <section class="card card-front" aria-label="Business card front">
    <div class="identity-panel">
      <p class="person-first">GERGELY</p>
      <p class="person-last">HALMINDO</p>
      <p class="person-title">Managing Director</p>
    </div>
    <div class="info-panel">
      <div class="brand-band">
        <span class="brand-square"></span>
        <span class="brand-name">Brask &amp; Partners</span>
      </div>
      <div class="contact-grid">
        <p class="contact-item">
          <span class="contact-icon"><svg viewBox="0 0 10 10"><path d="M5 0a3.4 3.4 0 0 0-3.4 3.4C1.6 6 5 10 5 10s3.4-4 3.4-6.6A3.4 3.4 0 0 0 5 0zm0 4.8a1.4 1.4 0 1 1 0-2.8 1.4 1.4 0 0 1 0 2.8z"/></svg></span>
          <span class="contact-text">1047 Budapest, Ravaszi str. 17/B, Hungary</span>
        </p>
        <p class="contact-item">
          <span class="contact-icon"><svg viewBox="0 0 10 10"><path d="M0 2h10v6H0zM1 3l4 2.6L9 3v-.2H1z" fill-rule="evenodd"/></svg></span>
          <span class="contact-text">g.halmindo@braskpartnera.hu</span>
        </p>
        <p class="contact-item">
          <span class="contact-icon"><svg viewBox="0 0 10 10"><path d="M2.2 0.5l1.6 2.2-1 1c.6 1.3 1.5 2.2 2.6 2.7l1-1 2.2 1.6-1 2C4.2 8.6 1.4 5.8 0.6 1.5z"/></svg></span>
          <span class="contact-text">+36 30 555 0192</span>
        </p>
        <p class="contact-item">
          <span class="contact-icon"><svg viewBox="0 0 10 10"><path d="M0 1h10v6.5H5.8V9h1.5v1H2.7V9h1.5V7.5H0zm1 1v4.5h8V2z"/></svg></span>
          <span class="contact-text">papernotejournal.com</span>
        </p>
        <p class="contact-item">
          <span class="contact-icon"><svg viewBox="0 0 10 10"><path d="M5 0a5 5 0 1 0 0 10A5 5 0 0 0 5 0zm0 1a4 4 0 0 1 3.9 3.5H1.1A4 4 0 0 1 5 1zM1.1 5.5h7.8a4 4 0 0 1-7.8 0z"/></svg></span>
          <span class="contact-text">www.braskpartnera.hu</span>
        </p>
      </div>
    </div>
  </section>

  <section class="card card-back" aria-label="Business card back">
    <span class="brand-square"></span>
    <span class="brand-name">Brask &amp; Partners</span>
  </section>

</body>
</html>
```